KINDRED: Social Media Post COVID-19 & Flu #1

- Create a similar design for a Social Media Post Image
- Attached, Logo, sample flu social media image.
- KINDRED - must be included - in the colors provided (see attachment)
- Protect your community. Protect Your Elders. Stay Vaccinated. - must be include
-COVID-19 & Flu - will be stated somewhere
- image of mom and sons
-might include boarder
- inspiration at https://volmerhaven.org/, and https://www.facebook.com/Volmerhaven

```html
<!DOCTYPE html>
<html lang="en">
<head>
<meta charset="utf-8">
<title>KINDRED – Flu &amp; COVID-19 Vaccination Campaign</title>
<link rel="stylesheet" href="https://fonts.googleapis.com/css2?family=Barlow:wght@500;600;800;900&display=swap">
<style>
  :root {
    --teal: #3f9fa9;
    --rust: #b0503f;
    --rust-deep: #a8473d;
    --panel: rgba(246, 244, 242, 0.86);
    --white: #ffffff;
    --border-a: #d8e4e4;
    --border-b: #c9c2c0;
  }
  * { margin: 0; padding: 0; box-sizing: border-box; }
  html, body { width: 1200px; height: 1200px; overflow: hidden; background: #ffffff; }
  .post {
    position: relative;
    width: 1200px;
    height: 1200px;
    overflow: hidden;
    font-family: "Barlow", Arial, sans-serif;
  }
  .frame-pattern {
    position: absolute;
    inset: 0;
    background: linear-gradient(135deg, var(--border-a), var(--border-b) 50%, var(--border-a));
  }
  .photo {
    position: absolute;
    left: 37px; top: 37px;
    width: 1126px; height: 1126px;
    background:
      linear-gradient(rgba(255,255,255,0.45), rgba(255,255,255,0.45)),
      linear-gradient(180deg, #c9d4dc 0%, #c8b08e 22%, #b59a7a 40%, #b98f86 62%, #9fae86 82%, #b7a3a4 100%);
  }
  .title-box {
    position: absolute;
    left: 79px; top: 79px;
    width: 746px; height: 200px;
    border: 7px solid var(--rust);
    background: rgba(255,255,255,0.55);
  }
  .title-box .name {
    position: absolute;
    left: 0; right: 0; top: 6px;
    text-align: center;
    color: var(--teal);
    font-weight: 500;
    font-size: 170px;
    line-height: 1;
    letter-spacing: 2px;
  }
  .campaign-band {
    position: absolute;
    left: 125px; top: 254px;
    width: 648px; height: 48px;
    background: var(--rust);
    color: var(--white);
    font-weight: 600;
    font-size: 33px;
    line-height: 48px;
    text-align: center;
    letter-spacing: 1px;
  }
  .org-mark {
    position: absolute;
    left: 861px; top: 78px;
    width: 254px; height: 205px;
    background: var(--white);
    display: flex;
    flex-direction: column;
    align-items: center;
    justify-content: center;
    gap: 14px;
  }
  .org-mark .badge {
    width: 46px; height: 46px;
    background: var(--teal);
  }
  .org-mark .org-name {
    color: var(--teal);
    font-weight: 600;
    font-size: 24px;
    line-height: 1.1;
    text-align: center;
    letter-spacing: 0.5px;
  }
  .message {
    position: absolute;
    left: 86px;
    width: 1031px;
    height: 133px;
    background: var(--panel);
    box-shadow: 0 3px 6px rgba(0,0,0,0.25);
    display: flex;
    align-items: center;
    justify-content: center;
    font-weight: 900;
    line-height: 1;
    white-space: nowrap;
  }
  .message .verb { color: var(--rust-deep); }
  .message .object { color: var(--teal); }
  .message.community { top: 532px; font-size: 90px; }
  .message.elders { top: 711px; font-size: 90px; }
  .message.vaccinated { top: 894px; font-size: 112px; }
</style>
</head>
<body>
<main class="post">
  <div class="frame-pattern" role="img" aria-label="Zigzag woven-style border pattern in teal and rust"></div>
  <div class="photo" role="img" aria-label="Photo of a smiling mother with her two sons sitting together on a patterned blanket outdoors under autumn trees"></div>

  <header class="title-box">
    <h1 class="name">KINDRED</h1>
  </header>
  <div class="campaign-band">FLU &amp; COVID -19 VACCINATION CAMPAIGN</div>

  <div class="org-mark">
    <span class="badge"></span>
    <span class="org-name">VOLMERHAVEN<br>ELDER COUNCIL</span>
  </div>

  <p class="message community"><span class="verb">Protect</span>&nbsp;<span class="object">Your Community.</span></p>
  <p class="message elders"><span class="verb">Protect</span>&nbsp;<span class="object">Your Elders.</span></p>
  <p class="message vaccinated"><span class="verb">Stay</span>&nbsp;<span class="object">Vaccinated.</span></p>
</main>
</body>
</html>
```